Brightwell Systems - Company Overview Brochure

We would like a single page A4 Brochure to give to new potential customers to provide a quick overview of our company. This will be used in presales meetings.

We have included the content we would like on the brochure under "Brightwell Systems Marketing Brochure.docx".

We have included two other designs "timebundleterms v4.pdf and Brightwell Public Cloud Plans.pdf" which shows similar marketing brochures we have. We would like these designs to have the same Brightwell Blue and "Specialised Technology Consultancy firm" theme.

Target Market(s)

Technology Sector

Industry/Entity Type

Information Technology

Colors
0054AA
0677BA
7BADD7
CADEEF
E8F1F8

Requirements
Must have
• "Innovative Tech Company Theme".

```html
<!DOCTYPE html>
<html lang="en">
<head>
<meta charset="utf-8">
<title>Brightwell Systems – Company Overview</title>
<link rel="stylesheet" href="https://fonts.googleapis.com/css2?family=Montserrat:wght@500;600;700;800&family=Open+Sans:wght@400;600&display=swap">
<style>
:root{
  --blue-deep:#0a1f5c;
  --blue-navy:#0c2a78;
  --blue-brand:#0054AA;
  --blue-mid:#0677BA;
  --blue-soft:#7BADD7;
  --blue-pale:#CADEEF;
  --blue-mist:#E8F1F8;
  --ink:#14213d;
  --grey:#4a5568;
  --white:#ffffff;
}
*{box-sizing:border-box;margin:0;padding:0}
html,body{width:1200px;height:1036px;overflow:hidden;background:#fff}
body{position:relative;font-family:"Open Sans",Arial,sans-serif;color:var(--ink)}
.sheet{position:absolute;left:289px;top:17px;width:808px;height:1143px;transform:scale(0.773);transform-origin:0 0;background:var(--white);overflow:hidden;box-shadow:0 0 0 1px #d9dee6}
.abs{position:absolute}
.hero{left:0;top:140px;width:808px;height:820px;background:linear-gradient(180deg,var(--blue-navy),var(--blue-deep))}
.header{left:0;top:0;width:808px;height:175px}
.brand{left:40px;top:52px;display:flex;align-items:center;gap:14px}
.brand-mark{width:46px;height:46px;background:var(--blue-brand)}
.brand-name{font-family:"Montserrat",sans-serif;font-weight:800;font-size:30px;color:var(--blue-navy);letter-spacing:1px;line-height:1}
.tagline{left:110px;top:104px;font-family:"Montserrat",sans-serif;font-weight:600;font-style:italic;font-size:15px;color:var(--blue-navy);display:flex;align-items:center;gap:8px}
.tagline::before,.tagline::after{content:"";width:28px;height:1px;background:var(--blue-brand)}
.photo{left:0;top:145px;width:420px;height:660px;background:radial-gradient(circle at 68% 30%,#3f7fe0 0,#1a4aa8 22%,transparent 55%),linear-gradient(90deg,#08184a,#123a8f 55%,rgba(12,42,120,0))}
.slogan{left:20px;top:760px;transform:rotate(-90deg);transform-origin:0 0;font-family:"Montserrat",sans-serif;font-weight:800;font-size:66px;line-height:76px;color:rgba(202,222,239,.55);letter-spacing:2px;white-space:nowrap}
.overview{left:470px;top:165px;width:270px;color:var(--white)}
h2{font-family:"Montserrat",sans-serif;font-weight:700;font-size:17px;letter-spacing:.3px}
.bar{width:40px;height:3px;background:var(--blue-mid);margin:8px 0 12px}
.overview p{font-size:9.3px;line-height:13.2px;margin-bottom:8px;color:#e6eefb}
.values{left:345px;top:365px;width:440px;display:flex}
.value{flex:1;text-align:center;color:var(--blue-soft);font-family:"Montserrat",sans-serif;font-size:8px;font-weight:600;line-height:11px;border-right:1px solid rgba(123,173,215,.35)}
.value:last-child{border:none}
.value b{color:var(--white);font-weight:600}
.value svg{display:block;margin:0 auto 6px;width:32px;height:32px;stroke:var(--blue-pale);fill:none;stroke-width:1.6}
.services{left:185px;top:450px;width:623px;height:347px;background:var(--white);clip-path:polygon(20px 0,100% 0,100% 100%,0 100%,0 20px)}
.services-title{left:0;top:12px;width:623px;text-align:center;font-family:"Montserrat",sans-serif;font-weight:700;font-size:18px;color:var(--blue-navy);display:flex;align-items:center;justify-content:center;gap:14px}
.services-title::before,.services-title::after{content:"";width:125px;height:1px;background:#c7d0dd}
.grid{left:19px;top:43px;width:557px;display:grid;grid-template-columns:repeat(4,1fr);border:1px solid #dde3ec}
.svc{height:145px;border-right:1px solid #dde3ec;border-bottom:1px solid #dde3ec;text-align:center;padding:10px 8px 0}
.svc:nth-child(4n){border-right:none}
.svc:nth-child(n+5){border-bottom:none}
.svc svg{width:48px;height:48px;stroke:var(--blue-brand);fill:none;stroke-width:2}
.svc h3{font-family:"Montserrat",sans-serif;font-weight:700;font-size:10.5px;color:var(--blue-navy);margin:8px 0 5px}
.svc p{font-size:8px;line-height:12px;color:var(--grey)}
.shield{left:40px;top:785px;width:150px;height:160px;background:radial-gradient(circle at 50% 45%,#8aa6cf 0,#2f5fb5 45%,rgba(10,31,92,0) 72%)}
.commit{left:204px;top:812px;width:250px;color:var(--white)}
.policy{left:478px;top:812px;width:290px;color:var(--white)}
.divider{left:456px;top:815px;width:1px;height:135px;background:rgba(123,173,215,.4)}
.commit h2,.policy h2{font-size:14px;color:var(--blue-soft)}
.lede{font-size:9px;line-height:13px;margin-bottom:6px}
ul.ticks{list-style:none}
ul.ticks li{font-size:8.2px;line-height:16.3px;padding-left:14px;position:relative}
ul.ticks li::before{content:"";position:absolute;left:0;top:4px;width:8px;height:8px;border-radius:50%;background:var(--blue-mid)}
ul.ticks li::after{content:"";position:absolute;left:2px;top:6px;width:3px;height:2px;border-left:1.2px solid #fff;border-bottom:1.2px solid #fff;transform:rotate(-45deg)}
.contact{left:50px;top:972px;width:230px}
.contact h2{font-size:14.5px;color:var(--blue-brand)}
.contact ul{list-style:none}
.contact li{display:flex;align-items:center;gap:12px;font-size:10.5px;height:23px}
.contact svg{width:15px;height:15px;fill:var(--blue-navy)}
.pillars{left:280px;top:975px;width:500px;display:flex}
.pillar{flex:1;text-align:center;border-left:1px solid #dde3ec;padding-top:5px}
.pillar svg{width:48px;height:48px;stroke:var(--blue-brand);fill:none;stroke-width:3}
.pillar h3{font-family:"Montserrat",sans-serif;font-weight:700;font-size:10.5px;color:var(--blue-brand);margin:8px 0 5px}
.pillar p{font-size:8.3px;line-height:13.5px;color:var(--grey)}
</style>
</head>
<body>
<div class="sheet">
  <div class="abs hero"></div>
  <div class="abs photo" role="img" aria-label="Data centre corridor with glowing cloud above a city skyline"></div>
  <div class="abs slogan">DO IT ONCE,<br>DO IT RIGHT</div>

  <svg class="abs header" viewBox="0 0 808 175" aria-hidden="true">
    <path d="M0 0H808V120Q400 160 0 140Z" fill="#fff"/>
    <path d="M500 0H660L580 110Z" fill="#e3e7ee"/>
    <path d="M560 120L660 0H808V175Z" fill="#0054AA"/>
    <path d="M650 0H808V175L660 70Z" fill="#0a1f5c"/>
    <path d="M600 118L760 0" stroke="#fff" stroke-width="1.5"/>
    <path d="M660 70L808 175" stroke="#fff" stroke-width="1.5"/>
  </svg>
  <div class="abs brand"><span class="brand-mark"></span><span class="brand-name">BRIGHTWELL SYSTEMS</span></div>
  <div class="abs tagline">Specialised Consulting</div>

  <section class="abs overview">
    <h2>COMPANY OVERVIEW</h2><div class="bar"></div>
    <p>Brightwell Systems is a specialised technology consulting company based in Perth, Western Australia. We deliver tailored, enterprise-grade solutions that help organisations build secure, resilient and efficient technology environments.</p>
    <p>Our expertise spans infrastructure, cybersecurity, cloud platforms, virtualisation, business continuity and strategic technology consulting. We work closely with our clients to understand their business objectives and design solutions that deliver long-term value.</p>
  </section>

  <div class="abs values">
    <div class="value"><svg viewBox="0 0 32 32"><path d="M4 12l8-6 6 2 6-2 4 8-3 9-8 3-6-3-6-2z"/></svg><b>AUSTRALIAN</b><br><b>BASED</b></div>
    <div class="value"><svg viewBox="0 0 32 32"><circle cx="16" cy="8" r="3"/><circle cx="8" cy="10" r="2.5"/><circle cx="24" cy="10" r="2.5"/><path d="M6 26l2-5 2 5-4-3h4zM14 26l2-5 2 5-4-3h4zM22 26l2-5 2 5-4-3h4z"/></svg>SPECIALISED<br><b>EXPERTISE</b></div>
    <div class="value"><svg viewBox="0 0 32 32"><path d="M16 3l11 4v8c0 7-5 12-11 14C10 27 5 22 5 15V7z"/><path d="M11 16l4 4 7-8"/></svg>SECURITY<br><b>FOCUSED</b></div>
    <div class="value"><svg viewBox="0 0 32 32"><path d="M2 12l7-4 7 4 7-4 7 4M6 14l8 8 4-3 4 3 6-8M14 22l-3-3"/></svg>CLIENT<br><b>PARTNERSHIP</b></div>
    <div class="value"><svg viewBox="0 0 32 32"><path d="M5 28V22h4v6M12 28V18h4v10M19 28V14h4v10M26 28V10"/><path d="M5 16l8-6 5 3 10-9M24 4h4v4"/></svg>BUSINESS<br><b>OUTCOMES</b></div>
  </div>

  <section class="abs services">
    <h2 class="abs services-title">SERVICES OVERVIEW</h2>
    <div class="abs grid">
      <div class="svc"><svg viewBox="0 0 48 48"><path d="M24 4l16 6v12c0 11-8 18-16 21C16 40 8 33 8 22V10z"/><rect x="18" y="22" width="12" height="10" fill="#0054AA"/><path d="M20 22v-4a4 4 0 018 0v4"/></svg><h3>CYBERSECURITY</h3><p>Protecting your business with end-to-end security strategies, risk management and threat protection.</p></div>
      <div class="svc"><svg viewBox="0 0 48 48"><path d="M12 36h26a8 8 0 000-16 12 12 0 00-23-3A9 9 0 0012 36z"/></svg><h3>CLOUD SOLUTIONS</h3><p>Secure, scalable and flexible cloud platforms designed for performance, reliability and growth.</p></div>
      <div class="svc"><svg viewBox="0 0 48 48"><rect x="6" y="6" width="36" height="10"/><rect x="6" y="19" width="36" height="10"/><rect x="6" y="32" width="36" height="10"/><path d="M28 6v36"/></svg><h3>INFRASTRUCTURE</h3><p>Design, build and optimise robust infrastructure that powers your critical operations.</p></div>
      <div class="svc"><svg viewBox="0 0 48 48"><path d="M24 14l9 3v6c0 6-4 9-9 11-5-2-9-5-9-11v-6z" fill="#0a1f5c"/><path d="M8 24a16 16 0 0127-12M40 24a16 16 0 01-27 12M35 6v6h-6M13 42v-6h6"/></svg><h3>BUSINESS CONTINUITY</h3><p>Ensure resilience and rapid recovery with comprehensive continuity and disaster recovery plans.</p></div>
      <div class="svc"><svg viewBox="0 0 48 48"><circle cx="24" cy="12" r="7" fill="#0054AA"/><path d="M10 44v-10a14 10 0 0128 0v10z"/><path d="M24 24l-2 6 2 10 2-10z" fill="#0a1f5c"/></svg><h3>CONSULTING</h3><p>Strategic technology advice aligned with your business goals, processes and roadmap.</p></div>
      <div class="svc"><svg viewBox="0 0 48 48"><rect x="4" y="8" width="28" height="24"/><rect x="24" y="12" width="20" height="24"/><path d="M10 40h28M18 32v8M8 16h14M28 18h12M28 24h12M28 30h12"/></svg><h3>VIRTUALISATION</h3><p>Maximise efficiency and agility through modern virtualisation technologies.</p></div>
      <div class="svc"><svg viewBox="0 0 48 48"><circle cx="24" cy="24" r="12"/><circle cx="24" cy="24" r="5" fill="#0054AA"/><path d="M24 6v6M24 36v6M6 24h6M36 24h6M11 11l4 4M33 33l4 4M37 11l-4 4M15 33l-4 4"/></svg><h3>MANAGED SERVICES</h3><p>Proactive monitoring, support and management to keep your environment running at its best.</p></div>
      <div class="svc"><svg viewBox="0 0 48 48"><path d="M24 10l12 7v14l-12 7-12-7V17z"/><circle cx="24" cy="8" r="4"/><circle cx="38" cy="16" r="4"/><circle cx="38" cy="32" r="4"/><circle cx="24" cy="40" r="4"/><circle cx="10" cy="32" r="4"/><circle cx="10" cy="16" r="4"/></svg><h3>ENTERPRISE ARCHITECTURE</h3><p>Architecture frameworks that align technology with business strategy and innovation.</p></div>
    </div>
  </section>

  <div class="abs shield" role="img" aria-label="Glowing metallic security shield on a digital platform"></div>

  <section class="abs commit">
    <h2>OUR COMMITMENT</h2><div class="bar"></div>
    <ul class="ticks">
      <li>Deliver secure, reliable and future-ready solutions</li>
      <li>Understand your business and deliver real outcomes</li>
      <li>Act with integrity, transparency and accountability</li>
      <li>Invest in skills, innovation and continuous improvement</li>
      <li>Build long-term partnerships you can trust</li>
    </ul>
  </section>
  <div class="abs divider"></div>
  <section class="abs policy">
    <h2>OUR POLICY</h2><div class="bar" style="background:transparent;margin:6px 0"></div>
    <p class="lede">We are committed to delivering high-quality, secure and compliant solutions through:</p>
    <ul class="ticks">
      <li>Upholding the highest standards of information security</li>
      <li>Complying with relevant legal and regulatory requirements</li>
      <li>Protecting client data and ensuring confidentiality</li>
      <li>Continuously improving our systems and services</li>
      <li>Promoting a culture of safety, respect and responsibility</li>
    </ul>
  </section>

  <section class="abs contact">
    <h2>CONTACT INFORMATION</h2><div class="bar"></div>
    <ul>
      <li><svg viewBox="0 0 16 16"><path d="M8 1a5 5 0 00-5 5c0 4 5 9 5 9s5-5 5-9a5 5 0 00-5-5zm0 7a2 2 0 110-4 2 2 0 010 4z"/></svg>Perth, Western Australia</li>
      <li><svg viewBox="0 0 16 16"><path d="M3 1l3 3-2 2c1 2 3 4 5 5l2-2 3 3-2 3C6 15 1 10 1 3z"/></svg>+61 (0)8 5550 1234</li>
      <li><svg viewBox="0 0 16 16"><path d="M1 3h14v10H1zM1 3l7 6 7-6" fill="none" stroke="#0a1f5c" stroke-width="1.6"/></svg>hello@brightwellsys.com.au</li>
      <li><svg viewBox="0 0 16 16"><circle cx="8" cy="8" r="7"/><path d="M1 8h14M8 1c3 3 3 11 0 14M8 1c-3 3-3 11 0 14" stroke="#fff" fill="none"/></svg>www.brightwellsys.com.au</li>
    </ul>
  </section>

  <div class="abs pillars">
    <div class="pillar"><svg viewBox="0 0 48 48"><circle cx="22" cy="26" r="17"/><circle cx="22" cy="26" r="9"/><circle cx="22" cy="26" r="2" fill="#0054AA"/><path d="M22 26L40 8M34 8h6v6"/></svg><h3>PRECISION</h3><p>Focused solutions designed to deliver measurable impact.</p></div>
    <div class="pillar"><svg viewBox="0 0 48 48"><path d="M24 4l16 6v12c0 11-8 18-16 21C16 40 8 33 8 22V10z" fill="#0054AA"/><path d="M16 24l6 6 10-12" stroke="#fff"/></svg><h3>PROTECTION</h3><p>Security and resilience built into everything we do.</p></div>
    <div class="pillar"><svg viewBox="0 0 48 48"><circle cx="24" cy="24" r="7" fill="#0054AA"/><circle cx="8" cy="8" r="5"/><circle cx="40" cy="8" r="5"/><circle cx="8" cy="40" r="5"/><circle cx="40" cy="40" r="5"/><path d="M12 12l7 7M36 12l-7 7M12 36l7-7M36 36l-7-7"/></svg><h3>PERFORMANCE</h3><p>Optimised technology for efficiency, speed and reliability.</p></div>
    <div class="pillar"><svg viewBox="0 0 48 48"><path d="M8 44V34M18 44V26M28 44V20M38 44V12" stroke-width="7"/><path d="M6 26l12-10 8 4 14-14M34 6h6v6"/></svg><h3>PARTNERSHIP</h3><p>Collaborative relationships built on trust, respect and results.</p></div>
  </div>

  <svg class="abs" style="left:0;top:1112px" width="808" height="31" viewBox="0 0 808 31" aria-hidden="true">
    <path d="M0 8H160L185 31H0Z" fill="#0a1f5c"/>
    <path d="M175 20H808V24H180Z" fill="#0054AA"/>
    <path d="M190 28H808V31H193Z" fill="#0a1f5c"/>
  </svg>
</div>
</body>
</html>
```